Business Card Design Project

We require a professional business card designed for our consulting organisation that has the same theme and colours as our logo except for the grey.

Colours on the front should predominately be white however some reference to our logo colours except for the grey.

The back of the card should be have background colour that aligns with our logo colour.

Layout, style and design is up to the designer. So send through your designs

Details are attached in the word document project brief.

Target Market(s)

Target market are large corporate organisations

Industry/Entity Type

Business

Requirements
Must have
• Content on the front must have:

Dale Fenwick
Managing Director

P: 0412 557 208
E: Dale@braviotraxgroup.com
W: www.braviotraxgroup.com

Content on the back must have the words:
Alliances
Placement
Training
Support

Design Colours
Must align to our logo

```html
<!DOCTYPE html>
<html lang="en">
<head>
<meta charset="utf-8">
<title>Bravio Trax Group – Business Cards</title>
<link rel="stylesheet" href="https://fonts.googleapis.com/css2?family=Arimo:wght@400;700&display=swap">
<style>
  :root {
    --stage: #2a2a2a;
    --brand-blue: #2b93d6;
    --ink: #3a3a3a;
    --ink-soft: #5a5a5a;
    --paper: #ffffff;
    --white: #ffffff;
  }
  * { box-sizing: border-box; margin: 0; padding: 0; }
  html, body {
    width: 1200px; height: 942px; overflow: hidden;
    background: var(--stage);
    font-family: "Arimo", Arial, sans-serif;
  }
  .stage {
    position: relative; width: 1200px; height: 942px;
    display: flex; align-items: center; justify-content: center; gap: 40px;
  }
  .card {
    position: relative; width: 520px; height: 318px; overflow: hidden;
    box-shadow: 0 10px 28px rgba(0,0,0,.45);
  }

  /* Back of card */
  .card--back { background: var(--brand-blue); color: var(--white); }
  .card--back .brand {
    position: absolute; left: 64px; top: 104px;
    display: flex; align-items: center; gap: 16px;
  }
  .card--back .brand-dot {
    width: 52px; height: 52px; border-radius: 50%;
    background: var(--white); flex: none;
  }
  .card--back .brand-name {
    font-weight: 700; font-size: 36px; line-height: 1; color: var(--white);
    letter-spacing: .5px; white-space: nowrap;
  }
  .services {
    position: absolute; left: 64px; right: 40px; bottom: 58px;
    display: flex; align-items: center; list-style: none;
    font-size: 14px; color: var(--white);
  }
  .services li { padding: 0 14px; border-left: 1px solid rgba(255,255,255,.85); line-height: 16px; }
  .services li:first-child { padding-left: 0; border-left: 0; }

  /* Front of card */
  .card--front { background: var(--paper); color: var(--ink); }
  .card--front .brand {
    position: absolute; left: 34px; top: 40px;
    display: flex; align-items: center; gap: 10px;
  }
  .card--front .brand-dot {
    width: 30px; height: 30px; border-radius: 50%;
    background: var(--brand-blue); flex: none;
  }
  .card--front .brand-name {
    font-weight: 700; font-size: 22px; line-height: 1; color: var(--brand-blue);
    white-space: nowrap;
  }
  .person { position: absolute; left: 34px; top: 128px; }
  .person-name { font-size: 30px; font-weight: 700; color: var(--ink); letter-spacing: .3px; line-height: 1.1; white-space: nowrap; }
  .person-role { margin-top: 6px; font-size: 15px; color: var(--brand-blue); }

  .contact {
    position: absolute; right: 28px; bottom: 28px;
    list-style: none; text-align: right;
    font-size: 13px; color: var(--ink-soft); line-height: 1.9;
  }
  .contact li { display: flex; justify-content: flex-end; align-items: center; gap: 8px; white-space: nowrap; }
  .contact .icon { width: 14px; height: 14px; flex: none; }
  .contact .phone { font-size: 17px; }
  .contact .web-prefix { color: var(--brand-blue); font-weight: 700; }
  .contact .spacer { width: 14px; flex: none; }
</style>
</head>
<body>
<main class="stage">

  <section class="card card--back" aria-label="Business card back">
    <div class="brand">
      <span class="brand-dot"></span>
      <span class="brand-name">Bravio Trax Group</span>
    </div>
    <ul class="services">
      <li>Alliances</li>
      <li>Placement</li>
      <li>Training</li>
      <li>Support</li>
    </ul>
  </section>

  <section class="card card--front" aria-label="Business card front">
    <div class="brand">
      <span class="brand-dot"></span>
      <span class="brand-name">Bravio Trax Group</span>
    </div>

    <div class="person">
      <p class="person-name">Dale Fenwick</p>
      <p class="person-role">Managing Director</p>
    </div>

    <ul class="contact">
      <li class="phone">0412 557 208
        <svg class="icon" viewBox="0 0 14 14" aria-hidden="true">
          <rect x="3" y="0.5" width="8" height="13" rx="1.5" fill="none" stroke="var(--brand-blue)" stroke-width="1.2"/>
          <rect x="4.5" y="2.5" width="5" height="7" fill="var(--brand-blue)"/>
        </svg>
      </li>
      <li>Dale@braviotraxgroup.com
        <svg class="icon" viewBox="0 0 14 14" aria-hidden="true">
          <rect x="0.5" y="2.5" width="13" height="9" fill="var(--brand-blue)"/>
          <path d="M0.5 2.5 L7 8 L13.5 2.5" fill="none" stroke="#fff" stroke-width="1.2"/>
        </svg>
      </li>
      <li><span><span class="web-prefix">www.</span>braviotraxgroup.com</span><span class="spacer"></span></li>
    </ul>
  </section>

</main>
</body>
</html>
```